Brackenford windows & Home Improvements

We are a family run business with over 35 years expertise. Myself and father run it
We supply and install a rated windows and all types of doors and
Veltrano composite doors .
We also specialise in renovating houses and adding extensions on to houses .
Are biggest selling point is the quality of the products we provide . we give 15 year guarantee on all windows and doors

I need flyers to distribute at shows and also to put through letterboxes
they can be a6 or a5 which ever works best . I have attached some images and our logo. Images don't have to be used

I have a show on the 29th march so need them fairly fast. Been designing them myself on this but they just don't look right

```html
<!DOCTYPE html>
<html lang="en">
<head>
<meta charset="utf-8">
<title>Brackenford Windows &amp; Home Improvements – Flyers</title>
<link href="https://fonts.googleapis.com/css2?family=Oswald:wght@400;500;600&family=Source+Sans+3:wght@400;600;700&display=swap" rel="stylesheet">
<style>
  :root{
    --blue:#1f50a0;
    --blue-dark:#143d80;
    --grey:#c8cacd;
    --grey-light:#e6e7e9;
    --white:#ffffff;
    --ink:#1a1a1a;
    --page:#efefef;
  }
  *{box-sizing:border-box;margin:0;padding:0}
  html,body{width:1200px;height:909px;overflow:hidden;background:var(--page)}
  body{position:relative;font-family:"Source Sans 3",Arial,sans-serif;color:var(--ink)}
  .flyer{position:absolute;width:520px;height:739px;background:var(--grey);overflow:hidden;box-shadow:0 4px 14px rgba(0,0,0,.18)}
  .flyer--about{left:50px;top:60px}
  .flyer--services{left:630px;top:114px;height:737px}
  .abs{position:absolute}
  .photo{position:absolute;background:linear-gradient(135deg,#8c8f8a,#5b6460 55%,#2f3440)}
  .brand-name{font-family:"Source Sans 3",Arial,sans-serif;font-weight:700;color:var(--blue);letter-spacing:.5px;line-height:1.15;text-transform:uppercase}
  .brand-mark{width:14px;height:14px;background:var(--blue);display:inline-block;flex:none}
  .headline{font-family:"Source Sans 3",Arial,sans-serif;text-align:center;color:var(--blue);line-height:1.18}
  .headline__main{font-size:27px;font-weight:600}
  .headline__sub{font-size:17px;font-weight:600}
  .badge{position:absolute;z-index:5;width:92px;height:92px;border-radius:50%;background:var(--blue);border:4px solid var(--white);box-shadow:0 3px 6px rgba(0,0,0,.35);color:var(--white);font-family:"Oswald",sans-serif;text-align:center;display:flex;flex-direction:column;justify-content:center;line-height:1.05}
  .badge__big{font-size:17px;font-weight:400}
  .badge__small{font-size:9px;font-weight:500}
  .footer{position:absolute;left:0;bottom:0;width:100%;height:87px;background:linear-gradient(180deg,var(--blue),var(--blue-dark));border-top:4px solid var(--grey-light);color:var(--white);text-align:center}
  .footer__cta{font-family:"Oswald",sans-serif;font-size:15px;margin-top:12px;letter-spacing:.2px}
  .footer__phones{font-family:"Oswald",sans-serif;font-size:25px;display:flex;align-items:center;justify-content:center;gap:12px;margin-top:2px;letter-spacing:.5px}
  .intro{position:absolute;left:24px;top:437px;width:472px;font-size:14.5px;line-height:1.25;text-align:justify}
  .intro strong{font-weight:700}
  .intro__tag{margin-top:14px;font-weight:700}
  .emergency{position:absolute;left:38px;top:578px;width:440px;height:38px;border:1.5px solid var(--blue);color:var(--blue);font-family:"Oswald",sans-serif;font-size:16px;display:flex;align-items:center;justify-content:center}
  .services__title{font-family:"Oswald",sans-serif;font-weight:500;color:var(--blue);font-size:36px;line-height:1}
  .services__sub{font-family:"Oswald",sans-serif;font-weight:500;color:var(--blue);font-size:18px;line-height:1}
  .service-list{list-style:none;font-size:17.5px;line-height:24.8px}
  .service-list li{display:flex;align-items:center;gap:7px}
  .service-list li::before{content:"";width:11px;height:11px;border-radius:50%;background:var(--blue);flex:none}
  .thumb{position:absolute;left:388px;width:112px;height:90px;border:3px solid var(--white);box-shadow:0 2px 5px rgba(0,0,0,.3)}
  .tagline{position:absolute;z-index:2;left:0;top:250px;width:384px;height:45px;background:var(--white);clip-path:polygon(0 0,360px 0,100% 100%,0 100%);font-weight:700;font-size:15.5px;display:flex;align-items:center;padding-left:14px}
</style>
</head>
<body>

<section class="flyer flyer--about">
  <div class="abs" style="left:0;top:273px;width:520px;height:142px;background:linear-gradient(180deg,#fff,#f2f2f3)"></div>
  <div class="abs" style="left:0;top:415px;width:520px;height:240px;background:linear-gradient(180deg,var(--grey),var(--grey-light))"></div>
  <div class="photo" style="left:0;top:0;width:520px;height:273px" role="img" aria-label="Photos of a white sash window, a stone pillar with gable house, and a black composite front door"></div>
  <svg class="abs" style="left:0;top:0" width="520" height="273" viewBox="0 0 520 273" aria-hidden="true">
    <polygon points="90,0 122,0 180,273 158,273" fill="var(--blue)"/>
    <polygon points="430,0 460,0 418,273 388,273" fill="var(--blue)"/>
  </svg>
  <div class="badge" style="left:408px;top:208px">
    <span class="badge__big">15 YEAR</span>
    <span class="badge__small">GUARANTEE</span>
    <span class="badge__small">ON ALL WINDOWS</span>
    <span class="badge__small">AND DOORS</span>
  </div>
  <div class="abs" style="left:30px;top:332px;display:flex;align-items:center;gap:8px">
    <span class="brand-mark"></span>
    <div class="brand-name" style="font-size:15px">Brackenford Windows<br>&amp; Home Improvements</div>
  </div>
  <div class="headline abs" style="left:258px;top:318px;width:254px">
    <div class="headline__main">SUPPLY &amp; INSTALL</div>
    <div class="headline__sub">WINDOWS, DOORS AND<br>VELTRANO COMPOSITE DOORS</div>
  </div>
  <div class="intro">
    <p><strong>Brackenford Windows &amp; Home Improvements</strong> is a family run business that offer full project management from initial contact to final fitting. Making sure all projects are finished to the highest standards and customers are fully satisfied.</p>
    <p class="intro__tag">Over 35 years expertise!</p>
  </div>
  <div class="emergency">EMERGENCY CALL OUT TO REPLACE BROKEN GLASS OR SECURE HOMES</div>
  <footer class="footer">
    <div class="footer__cta">CALL TODAY FOR YOUR FREE QUOTE</div>
    <div class="footer__phones">
      <svg width="32" height="32" viewBox="0 0 32 32" aria-hidden="true"><circle cx="16" cy="16" r="12" fill="none" stroke="#fff" stroke-width="2.5"/><text x="16" y="19.5" font-size="9" font-family="Oswald,sans-serif" fill="#fff" text-anchor="middle">24</text><path d="M4 22c2 5 6 8 11 9l2-3-3-2-2 1c-2-1-3-3-4-5l1-2-2-3z" fill="#fff"/></svg>
      <span>087-5550142 / 085-5550176</span>
    </div>
  </footer>
</section>

<section class="flyer flyer--services">
  <div class="abs" style="left:0;top:0;width:520px;height:272px;background:var(--blue)"></div>
  <div class="photo" style="left:0;top:0;width:300px;height:250px;background:linear-gradient(135deg,#7c8aa3,#c9a15a 55%,#8a6a3a)" role="img" aria-label="Tradesman wearing a tool belt holding a red cordless drill"></div>
  <div class="abs" style="left:320px;top:52px;width:195px;display:flex;align-items:center;gap:8px;justify-content:center">
    <span class="brand-mark" style="background:var(--white)"></span>
    <div class="brand-name" style="font-size:13px;color:var(--white)">Brackenford Windows<br>&amp; Home Improvements</div>
  </div>
  <div class="headline abs" style="left:272px;top:116px;width:246px;color:var(--white)">
    <div class="headline__main">SUPPLY &amp; INSTALL</div>
    <div class="headline__sub">WINDOWS, DOORS AND<br>VELTRANO COMPOSITE DOORS</div>
  </div>
  <div class="badge" style="left:424px;top:196px">
    <span class="badge__big">15 YEAR</span>
    <span class="badge__small">GUARANTEE</span>
    <span class="badge__small">ON ALL WINDOWS</span>
    <span class="badge__small">AND DOORS</span>
  </div>
  <div class="tagline">Family run business with over 35 years expertise!</div>
  <div class="abs" style="left:16px;top:312px">
    <h2 class="services__title">SERVICES:</h2>
    <ul class="service-list" style="margin-top:10px">
      <li>A rated windows double &amp; triple glazed</li>
      <li>All types of doors, patio ,French and UPVC</li>
      <li>Specialists in Veltrano Composite doors</li>
      <li>Sunrooms &amp; Conservatories</li>
    </ul>
    <h3 class="services__sub" style="margin-top:30px">HOME IMPROVEMENTS</h3>
    <ul class="service-list" style="margin-top:6px">
      <li>All types of home improvements</li>
      <li>Renovations</li>
      <li>Extensions</li>
      <li>Roofing</li>
      <li>Supply &amp; fit fascia soffit &amp; seamless gutters</li>
    </ul>
  </div>
  <div class="thumb" style="top:321px;background:linear-gradient(135deg,#6b5a45,#c7b79c)" role="img" aria-label="Renovated open-plan kitchen interior"></div>
  <div class="thumb" style="top:422px;background:linear-gradient(135deg,#9aa3a8,#8a5a35)" role="img" aria-label="Timber decking extension with glazed walls"></div>
  <div class="thumb" style="top:524px;background:linear-gradient(135deg,#8d9aa6,#a58562)" role="img" aria-label="Slate roof on a brick house"></div>
  <footer class="footer">
    <div class="footer__cta">CALL TODAY FOR YOUR FREE QUOTE</div>
    <div class="footer__phones">
      <svg width="32" height="32" viewBox="0 0 32 32" aria-hidden="true"><circle cx="16" cy="16" r="12" fill="none" stroke="#fff" stroke-width="2.5"/><text x="16" y="19.5" font-size="9" font-family="Oswald,sans-serif" fill="#fff" text-anchor="middle">24</text><path d="M4 22c2 5 6 8 11 9l2-3-3-2-2 1c-2-1-3-3-4-5l1-2-2-3z" fill="#fff"/></svg>
      <span>087-5550142 / 085-5550176</span>
    </div>
  </footer>
</section>

</body>
</html>
```